Business Card Design - Local Discount Club

Looking for a fun business card for a local discount club. One side should be the logo only and the other should be have :

Name
Title
Phone, Email
Website

```html
<!DOCTYPE html>
<html lang="en">
<head>
<meta charset="utf-8">
<title>Harbor Saver Club – Business Card</title>
<link rel="stylesheet" href="https://fonts.googleapis.com/css2?family=Montserrat:wght@500;700;800&display=swap">
<style>
  :root {
    --page-bg: #d8d3cc;
    --card-bg: #eeebe6;
    --navy: #2f4a99;
    --teal: #3f8ca6;
    --soft-teal: #7fbcc0;
    --soft-green: #b4cf86;
    --soft-navy: #7d8fc4;
    --text-dark: #2b2b2b;
  }
  * { margin: 0; padding: 0; box-sizing: border-box; }
  html, body {
    width: 1200px;
    height: 1047px;
    overflow: hidden;
    background: var(--page-bg);
    font-family: "Montserrat", sans-serif;
  }
  .card {
    position: absolute;
    left: 151px;
    top: 289px;
    width: 947px;
    height: 518px;
    border-radius: 24px;
    background: var(--card-bg);
    overflow: hidden;
    box-shadow: 0 10px 30px rgba(0,0,0,0.12);
  }
  .decor-area {
    position: absolute;
    left: 500px;
    top: 0;
    width: 447px;
    height: 518px;
    background: linear-gradient(100deg,
      var(--card-bg) 0%,
      var(--soft-green) 35%,
      var(--soft-teal) 65%,
      var(--soft-navy) 100%);
    opacity: 0.55;
  }

  .brand {
    position: absolute;
    left: 38px;
    top: 44px;
  }
  .brand__name {
    font-weight: 800;
    font-size: 46px;
    line-height: 1.12;
    color: var(--navy);
    letter-spacing: 0.5px;
    text-transform: uppercase;
  }

  .person {
    position: absolute;
    left: 36px;
    top: 276px;
  }
  .person__name {
    font-weight: 700;
    font-size: 36px;
    line-height: 1.1;
    color: var(--teal);
    letter-spacing: 1px;
  }
  .person__title {
    font-weight: 500;
    font-size: 21px;
    color: var(--text-dark);
    margin-top: 8px;
  }

  .contact {
    position: absolute;
    left: 36px;
    top: 381px;
    list-style: none;
  }
  .contact__item {
    display: flex;
    align-items: center;
    gap: 9px;
    font-size: 22px;
    font-weight: 500;
    color: var(--text-dark);
    height: 35px;
  }
  .contact__icon {
    width: 20px;
    height: 20px;
    fill: var(--teal);
    flex: none;
  }
</style>
</head>
<body>
  <section class="card">
    <div class="decor-area" role="img" aria-label="Soft decorative colour area in green, teal and navy"></div>

    <div class="brand">
      <p class="brand__name">The Harbor<br>Saver<br>Club</p>
    </div>

    <div class="person">
      <h1 class="person__name">DANIEL HART</h1>
      <p class="person__title">Managing Director</p>
    </div>

    <ul class="contact">
      <li class="contact__item">
        <svg class="contact__icon" viewBox="0 0 24 24" aria-hidden="true"><path d="M3 8c0-2 3-4 9-4s9 2 9 4v2h-5V8H8v2H3zM6 11h12l2 8H4z"/></svg>
        555 010 2030
      </li>
      <li class="contact__item">
        <svg class="contact__icon" viewBox="0 0 24 24" aria-hidden="true"><path d="M3 6h18v2l-9 6-9-6zM3 10l9 6 9-6v8H3z"/></svg>
        hello@harborsaver.com
      </li>
      <li class="contact__item">
        <svg class="contact__icon" viewBox="0 0 24 24" aria-hidden="true"><path d="M12 3a9 9 0 1 0 0 18a9 9 0 1 0 0-18zm0 2c1.2 1.5 2 4 2 7s-.8 5.5-2 7c-1.2-1.5-2-4-2-7s.8-5.5 2-7zM4.5 11h15v2h-15z" fill-rule="evenodd"/></svg>
        www.harborsaver.com
      </li>
    </ul>
  </section>
</body>
</html>
```